Darlene Whitcott

I need all of my logos on one card. I would like a burgundy back and Harbor Shield and Tamsworth insurance being the most prominent.
Phone Number 541-382-9154
Web:
www.Tamsworthins.example
www.Harbor Shield.example
www.Kell-Insurance.example

```html
<!DOCTYPE html>
<html lang="en">
<head>
<meta charset="utf-8">
<title>Tamsworth Insurance – Business Card</title>
<link href="https://fonts.googleapis.com/css2?family=Cinzel:wght@600;700&family=Tinos&display=swap" rel="stylesheet">
<style>
  :root {
    --backdrop: #6f4526;
    --white: #ffffff;
    --gold: #d4aa00;
    --gold-soft: #c9a227;
    --ink: #1a1a1a;
    --burgundy: #4a0f24;
    --rule-light: #d8c9cf;
  }
  * { margin: 0; padding: 0; box-sizing: border-box; }
  html, body { width: 1200px; height: 900px; overflow: hidden; }
  body { background: var(--backdrop); position: relative; }

  .card { position: absolute; width: 556px; height: 343px; overflow: hidden; }

  /* Front */
  .card-front { left: 329px; top: 90px; background: var(--white); }
  .card-front .bands { position: absolute; left: 0; top: 0; width: 556px; height: 343px; }
  .brand-front {
    position: absolute; left: 0; width: 100%; text-align: center;
    font-family: "Cinzel", serif; font-weight: 700; color: var(--gold);
  }
  .brand-front .name-main { top: 88px; font-size: 44px; letter-spacing: 2px; }
  .brand-front.name-main { top: 88px; font-size: 44px; letter-spacing: 2px; line-height: 1; }
  .brand-front.name-sub { top: 138px; font-size: 20px; letter-spacing: 5px; line-height: 1; }

  .contact {
    position: absolute; left: 0; top: 222px; width: 100%; text-align: center;
    font-family: "Tinos", "Times New Roman", serif; color: var(--ink); font-size: 17px;
  }
  .contact .phone-mail { line-height: 20px; }
  .contact .divider { width: 318px; height: 1px; background: #6b5600; margin: 9px auto 8px; }
  .contact .sites li { list-style: none; line-height: 23px; }

  /* Back */
  .card-back { left: 330px; top: 470px; background: var(--burgundy); }
  .brand-back {
    position: absolute; left: 0; width: 100%; text-align: center;
    font-family: "Cinzel", serif; font-weight: 700; color: var(--gold-soft); line-height: 1;
  }
  .brand-back.name-main { top: 92px; font-size: 46px; letter-spacing: 1px; }
  .brand-back.name-sub { top: 144px; font-size: 30px; letter-spacing: 2px; }
  .card-back .divider {
    position: absolute; left: 105px; top: 215px; width: 347px; height: 1px; background: var(--rule-light);
  }
  .partner {
    position: absolute; top: 258px; text-align: center;
    font-family: "Cinzel", serif; font-weight: 700; color: var(--gold-soft); line-height: 1.15;
  }
  .partner .line-1 { display: block; font-size: 17px; }
  .partner .line-2 { display: block; font-size: 10px; letter-spacing: 2px; }
  .partner-tamsworth { left: 100px; width: 200px; }
  .partner-kell { left: 290px; width: 190px; }
</style>
</head>
<body>

<section class="card card-front" aria-label="Business card front">
  <svg class="bands" viewBox="0 0 556 343" aria-hidden="true">
    <polygon points="0,178 556,190 556,343 0,343" fill="var(--ink)"/>
    <polygon points="0,195 556,197 556,343 0,343" fill="var(--gold)"/>
  </svg>
  <div class="brand-front name-main">TAMSWORTH</div>
  <div class="brand-front name-sub">INSURANCE</div>

  <div class="contact">
    <p class="phone-mail">P: 541-382-9154 | E:info@tamsworthins.example</p>
    <div class="divider"></div>
    <ul class="sites">
      <li>www.Tamsworthins.example</li>
      <li>www.Harbor Shield.example</li>
      <li>www.Kell-Insurance.example</li>
    </ul>
  </div>
</section>

<section class="card card-back" aria-label="Business card back">
  <div class="brand-back name-main">HARBOR SHIELD</div>
  <div class="brand-back name-sub">INC</div>
  <div class="divider"></div>
  <div class="partner partner-tamsworth">
    <span class="line-1">TAMSWORTH</span>
    <span class="line-2">INSURANCE</span>
    <span class="line-2">FARM &amp; RANCH</span>
  </div>
  <div class="partner partner-kell">
    <span class="line-1">WARREN KELL</span>
    <span class="line-2">AGENCY INC</span>
  </div>
</section>

</body>
</html>
```